business card with 2 locations on 1 card

I need a modern looking business card that I would use at 2 different locations. Possibly 1 location on 1 side and other location on other side. One should be able to distinguish the 2 locations immediately before having to read the address or description on card. You can take a look at my website to see what I'm drawn to. The logo is brand new that I just purchased on Craft Hive. I want to emphasize family.
Updates

Let's not use the yellow and blue colors. Added Thursday, August 31, 2017

Target Market(s)

women and children

Industry/Entity Type

Health And Wellness

Contact Information for Business Card

Business name: Willow Brook Chiropractic & Acupuncture
My name: Lorin Daske
Job title: DC, MSOM, LAc (NV), CCN

Location 1
Address: 4817 Marlowe Blvd, Suite C-210, Fenwick, TX 75391
Phone: (469) 555-0182
Fax: (972) 555-0137

Location 2
Address: 1936 Belvane Road, Suite 140, Ashgrove, TX 75482
Phone: (469) 555-0169
Fax: (972) 555-0137

Email: drlorindaske@mailnest.example
Website: www.drlorindaske.example

Font styles to use
Serif
Sans Serif

Colors

Designer to choose colors to be used in the design.

Requirements
Must have
• distinction between 2 locations.
Nice to have
• Colors preference below is there. But I like to see what you come up with too!

```html
<!DOCTYPE html>
<html lang="en">
<head>
<meta charset="utf-8">
<title>Willow Brook Chiropractic &amp; Acupuncture – Business Card</title>
<link rel="stylesheet" href="https://fonts.googleapis.com/css2?family=Marcellus&family=Cinzel:wght@500&family=Source+Sans+3:wght@400&display=swap">
<style>
  :root {
    --teal: #2c6e6e;
    --white: #ffffff;
    --backdrop: #ecebe8;
    --ink-light: #f2f6f6;
  }
  * { margin: 0; padding: 0; box-sizing: border-box; }
  html, body { width: 1200px; height: 900px; overflow: hidden; }
  body {
    background: var(--backdrop);
    position: relative;
    font-family: "Source Sans 3", "Helvetica Neue", Arial, sans-serif;
    color: var(--white);
  }
  .card {
    position: absolute;
    background: var(--teal);
    overflow: hidden;
    box-shadow: 0 6px 18px rgba(0,0,0,.18);
  }
  .card--front { left: 190px; top: 70px; width: 590px; height: 364px; }
  .card--back  { left: 415px; top: 485px; width: 565px; height: 350px; }

  .front-art { position: absolute; inset: 0; }
  .front-art__name {
    position: absolute; left: 258px; top: 150px; width: 300px;
    text-align: center; color: var(--teal);
    font-family: "Cinzel", Georgia, serif; font-weight: 500;
    font-size: 26px; line-height: 1.25;
  }

  .person { position: absolute; left: 31px; top: 28px; }
  .person__name {
    font-family: "Marcellus", Georgia, serif; font-weight: 400;
    font-size: 21px; letter-spacing: 1px; text-transform: uppercase;
    line-height: 1.2;
  }
  .person__title { font-size: 14px; margin-top: 2px; color: var(--ink-light); }

  .contact { position: absolute; font-size: 14.5px; line-height: 20px; color: var(--ink-light); }
  .contact__row { display: flex; align-items: flex-start; gap: 6px; }
  .contact__icon { width: 11px; height: 11px; flex: none; margin-top: 5px; fill: var(--white); }

  .front-online  { left: 31px; top: 84px; }
  .front-address { left: 31px; top: 222px; }
  .front-phones  { left: 31px; top: 295px; }

  .back-brand {
    position: absolute; left: 40px; top: 72px; width: 270px;
    text-align: center;
  }
  .back-brand__mark {
    width: 122px; height: 122px; margin: 0 auto 14px;
    border: 4px solid var(--white); border-radius: 50%;
  }
  .back-brand__name {
    font-family: "Cinzel", Georgia, serif; font-weight: 500;
    color: var(--white); font-size: 27px; line-height: 1.05;
  }
  .back-brand__sub {
    font-family: "Cinzel", Georgia, serif; font-weight: 500;
    color: var(--white); font-size: 12.5px; margin-top: 3px;
  }
  .back-address { left: 352px; top: 120px; }
  .back-phones  { left: 352px; top: 194px; }
</style>
</head>
<body>

<section class="card card--front" aria-label="Business card front, Fenwick location">
  <svg class="front-art" width="590" height="364" viewBox="0 0 590 364" aria-hidden="true">
    <rect x="410" y="0" width="180" height="364" fill="var(--white)"/>
    <circle cx="410" cy="178" r="176" fill="var(--white)"/>
    <circle cx="410" cy="178" r="182" fill="none" stroke="var(--teal)" stroke-width="12"/>
  </svg>
  <div class="front-art__name">Willow Brook</div>

  <div class="person">
    <h1 class="person__name">Lorin Daske</h1>
    <p class="person__title">DC, MSOM, LAc (NV), CCN</p>
  </div>

  <div class="contact front-online">
    <div class="contact__row">
      <svg class="contact__icon" viewBox="0 0 12 12"><path d="M0 2h12v8H0z"/><path d="M1 3l5 4 5-4" fill="none" stroke="var(--teal)" stroke-width="1"/></svg>
      <span>drlorindaske@mailnest.example</span>
    </div>
    <div class="contact__row">
      <svg class="contact__icon" viewBox="0 0 12 12"><circle cx="6" cy="6" r="5.5"/><path d="M0.5 6h11M6 0.5c-3 3-3 8 0 11M6 0.5c3 3 3 8 0 11" fill="none" stroke="var(--teal)" stroke-width="0.9"/></svg>
      <span>www.drlorindaske.example</span>
    </div>
  </div>

  <div class="contact front-address">
    <div class="contact__row">
      <svg class="contact__icon" viewBox="0 0 12 14"><path d="M6 0a4.5 4.5 0 0 0-4.5 4.5C1.5 8 6 14 6 14s4.5-6 4.5-9.5A4.5 4.5 0 0 0 6 0zm0 6.3a1.8 1.8 0 1 1 0-3.6 1.8 1.8 0 0 1 0 3.6z"/></svg>
      <span>4817 Marlowe Blvd,<br>Suite C-210, Fenwick,<br>TX 75391</span>
    </div>
  </div>

  <div class="contact front-phones">
    <div class="contact__row">
      <svg class="contact__icon" viewBox="0 0 12 12"><path d="M2.4 0.5l2 2.4-1.1 1.5c.8 1.7 2 2.9 3.7 3.7l1.5-1.1 2.4 2-1.2 2.3C4.5 11 1 7.5.2 1.7z"/></svg>
      <span>(469) 555-0182</span>
    </div>
    <div class="contact__row">
      <svg class="contact__icon" viewBox="0 0 12 12"><path d="M3 0h5l1 1v3H3z"/><path d="M0 4.5h12v7.5H0z"/><path d="M3 7h6v1H3zM3 9h6v1H3z" fill="var(--teal)"/></svg>
      <span>(972) 555-0137</span>
    </div>
  </div>
</section>

<section class="card card--back" aria-label="Business card back, Ashgrove location">
  <div class="back-brand">
    <div class="back-brand__mark"></div>
    <div class="back-brand__name">Willow Brook</div>
    <div class="back-brand__sub">Chiropractic &amp; Acupuncture</div>
  </div>

  <div class="contact back-address">
    <div class="contact__row">
      <svg class="contact__icon" viewBox="0 0 12 14"><path d="M6 0a4.5 4.5 0 0 0-4.5 4.5C1.5 8 6 14 6 14s4.5-6 4.5-9.5A4.5 4.5 0 0 0 6 0zm0 6.3a1.8 1.8 0 1 1 0-3.6 1.8 1.8 0 0 1 0 3.6z"/></svg>
      <span>1936 Belvane Road,<br>Suite 140,<br>Ashgrove, TX 75482</span>
    </div>
  </div>

  <div class="contact back-phones">
    <div class="contact__row">
      <svg class="contact__icon" viewBox="0 0 12 12"><path d="M2.4 0.5l2 2.4-1.1 1.5c.8 1.7 2 2.9 3.7 3.7l1.5-1.1 2.4 2-1.2 2.3C4.5 11 1 7.5.2 1.7z"/></svg>
      <span>(469) 555-0169</span>
    </div>
    <div class="contact__row">
      <svg class="contact__icon" viewBox="0 0 12 12"><path d="M3 0h5l1 1v3H3z"/><path d="M0 4.5h12v7.5H0z"/><path d="M3 7h6v1H3zM3 9h6v1H3z" fill="var(--teal)"/></svg>
      <span>(972) 555-0137</span>
    </div>
  </div>
</section>

</body>
</html>
```